Re-launching marine insurance adjusting company - looking for energy

I am a sole practitioner specializing in the profession of average adjusting. There is an on-line brochure at www.rkbtnova.com I am one of only a handful of specialists in this field and I enjoy a fair amount of name recognition, domestically in the US and internationally. My principal markets are the US, the London and Scandinavian insurance markets and shipowners and insurers in Latin America.
The business is a mixture of law, accounting and insurance and my clientele relies on a time-sensitive and accurate work-product, clearly stating an insurance company's liability for a given claim. The identity needs to project gravitas rather than flash.
Since 1998 I have traded as "The Halloway Company" but have also attempted to establish the name RKBNOVA.com so that people would visit my website.
I want to implement a single identity across my stationery, business cards and website. I have come to see "The Halloway Company" as rather fatuous, since there is no company, it is just me. The Internet domain RKBNOVA is long-established and I would be reluctant to change it. I have considered trading as simply Marcus T Halloway, MTH, RKBNOVA or attempting to come up with a name that could be abbreviated to MTH, e.g. M Halloway Trelantics - but I can't find a suitable word for the second S.
Logo-wise, I have considered a stylized MTH or RKBNOVA redolent of waves of the sea. A nautical theme embodying a cargo ship, navigational beacon or lighthouse might be appropriate but these tend to be hackneyed.
I have attached a card that I mocked up at Pix, connoting stacking up numbers, which I really like, but I think it is too cryptic for people in most insurance companies, who don't particularly think laterally or they wouldn't work in marine insurance, and the card that I use currently, which I intended to be understated, but in fact it states nothing.
I have also attached my current letterhead, to demonstrate how I really need help.
Finally, I have attached a credentials sheet, to attempt to establish how narrow and deep is the professional niche that I occupy.
What I am looking to implement is a single logo, font, them and color scheme to use across my website, letterhead and business cards.
Over to the Sketch Guild...
Target Market(s)
Ship owners and insurance companies
Industry/Entity Type
Accounting

```html
<!DOCTYPE html>
<html lang="en">
<head>
<meta charset="utf-8">
<title>RKBNOVA Letterhead</title>
<link rel="stylesheet" href="https://fonts.googleapis.com/css2?family=Montserrat:wght@400;600&display=swap">
<style>
  :root {
    --backdrop: #8f9095;
    --paper: #ffffff;
    --navy: #283278;
    --sky: #33a3dc;
    --ink-light: #ffffff;
  }
  html, body {
    margin: 0;
    padding: 0;
    width: 1200px;
    height: 1000px;
    overflow: hidden;
    background: var(--backdrop);
    font-family: "Montserrat", Arial, sans-serif;
  }
  .letterhead {
    position: absolute;
    left: 252px;
    top: 50px;
    width: 696px;
    height: 900px;
    background: var(--paper);
    box-shadow: 0 2px 10px rgba(0,0,0,0.18);
    overflow: hidden;
  }
  .brand {
    position: absolute;
    top: 78px;
    right: 62px;
    display: flex;
    align-items: center;
    gap: 10px;
  }
  .brand-dot {
    width: 14px;
    height: 14px;
    border-radius: 50%;
    background: var(--sky);
  }
  .brand-name {
    font-weight: 600;
    font-size: 30px;
    letter-spacing: 1px;
    color: var(--navy);
  }
  .footer-rule {
    position: absolute;
    left: 0;
    right: 0;
    bottom: 61px;
    height: 6px;
    background: var(--navy);
  }
  .footer-band {
    position: absolute;
    left: 0;
    right: 0;
    bottom: 0;
    height: 55px;
    box-sizing: border-box;
    padding: 0 24px;
    background: var(--sky);
    display: flex;
    align-items: center;
    justify-content: space-between;
    color: var(--ink-light);
    font-size: 8.5px;
    font-weight: 400;
  }
  .contact-item {
    display: flex;
    align-items: center;
    gap: 5px;
    white-space: nowrap;
  }
  .contact-item svg {
    width: 8px;
    height: 8px;
    flex: none;
    fill: var(--ink-light);
  }
</style>
</head>
<body>
  <main class="letterhead">
    <header class="brand">
      <span class="brand-dot"></span>
      <span class="brand-name">RKBNOVA</span>
    </header>

    <div class="footer-rule"></div>
    <footer class="footer-band">
      <span class="contact-item">
        <svg viewBox="0 0 10 10" aria-hidden="true"><path d="M1 2.5C1 1.7 1.7 1 2.5 1h5C8.3 1 9 1.7 9 2.5V3.5H7V2.8H3v.7H1z"/><rect x="1.5" y="4.5" width="7" height="4.5" rx="1"/></svg>
        (646) 555 0172
      </span>
      <span class="contact-item">
        <svg viewBox="0 0 10 10" aria-hidden="true"><rect x="3" y="1" width="4" height="3"/><rect x="1" y="4" width="8" height="4" rx="1"/><rect x="3" y="7" width="4" height="2.5"/></svg>
        (646) 555 0188
      </span>
      <span class="contact-item">
        <svg viewBox="0 0 10 10" aria-hidden="true"><path d="M1 2h8v1L5 5.5 1 3z"/><path d="M1 4l4 2.5L9 4v4H1z"/></svg>
        info@rkbnova.com
      </span>
      <span class="contact-item">
        <svg viewBox="0 0 10 10" aria-hidden="true"><path d="M5 .5a4.5 4.5 0 1 0 0 9 4.5 4.5 0 0 0 0-9zm0 1.3c.6.7 1 1.8 1.1 2.7H3.9C4 3.6 4.4 2.5 5 1.8zm-1.1 3.7h2.2c-.1.9-.5 2-1.1 2.7-.6-.7-1-1.8-1.1-2.7z"/></svg>
        www.rkbnova.com
      </span>
      <span class="contact-item">
        <svg viewBox="0 0 10 10" aria-hidden="true"><path d="M5 .5A3.3 3.3 0 0 0 1.7 3.8C1.7 6.3 5 9.5 5 9.5s3.3-3.2 3.3-5.7A3.3 3.3 0 0 0 5 .5zm0 4.6a1.3 1.3 0 1 1 0-2.6 1.3 1.3 0 0 1 0 2.6z"/></svg>
        48 Harbor Crest Rd, Portsmouth, NH 03801, USA
      </span>
    </footer>
  </main>
</body>
</html>
```